milvetra
Zielgruppe
Produktentwicklung und Konstruktion von technischen Komponenten und Anlagen mit der Schwerpunkt OFF-HIGHWAY Batteriegehäuse für Lithium-Ionen-Batterien. Unter OFF-HIGHWAY versteht man vor allem Nutzfahrzeuge, die OHNE Kennzeichen auf Baustellen, in der Landwirtschaft etc. eingesetzt werden. 'Batteriegehäuse' sind grob vereinbart Kästen aus Stahl, Edelstahl, Aluminium oder Kunststoff, die die Batteriemodule aufnehmen und gegen äußere Einflüsse schützen (Staub, Wasser, mechanische Beschädigung etc.).
Zielgruppen sind vorrangig bestehende Unternehmen (meist Mittelständler), die OFF-HIGHWAY Fahrzeuge bisher mit Verbrennungsmotoren ausgestattet haben und diese nun mit Elektroantrieb ausrüsten (Neufahrzeuge) oder nachrüsten (bestehende Fahrzeuge) wollen/müssen.
Aufgabenstellung
www.plutek.de (Aufbau ähnelt dem von uns gewünschten
www.lumvasa.de (optisch sehr ansprechend)

```html
<!DOCTYPE html>
<html lang="de">
<head>
<meta charset="utf-8">
<title>milvetra case engineering</title>
<link rel="stylesheet" href="https://fonts.googleapis.com/css2?family=Bebas+Neue&family=Open+Sans:wght@400;600;700&display=swap">
<style>
:root{
  --red:#c41a22;
  --red-dark:#6b1215;
  --red-deep:#5e0f12;
  --ink:#222;
  --text:#444;
  --grey-box:#d6d6d6;
  --grey-light:#f1f1f1;
  --placeholder-a:#e9e6e2;
  --placeholder-b:#d9d4ce;
  --topbar:#2f2f2f;
  --footer:#1d2030;
  --footer-bottom:#33363f;
  --white:#fff;
}
*{box-sizing:border-box;margin:0;padding:0}
html,body{width:1200px;height:3908px;overflow:hidden}
body{position:relative;background:var(--white);font-family:"Open Sans",Arial,sans-serif;color:var(--text);font-size:13px}
.abs{position:absolute}
.display{font-family:"Bebas Neue",Impact,sans-serif;font-weight:400;color:var(--ink);letter-spacing:1px}
.btn{position:absolute;background:var(--red);color:var(--white);font-size:9px;font-weight:700;letter-spacing:1.5px;display:flex;align-items:center;justify-content:center;text-transform:uppercase}

/* top bar */
.topbar{left:0;top:0;width:1200px;height:27px;background:var(--topbar);color:#eee;font-size:9px}
.topbar .contact{position:absolute;left:28px;top:8px}
.topbar .social{position:absolute;right:34px;top:9px;display:flex;gap:13px}
.topbar .social span{width:9px;height:9px;border-radius:50%;background:#ddd}

/* header */
.header{left:0;top:27px;width:1200px;height:72px;background:var(--white);border-bottom:1px solid #e6e6e6}
.brand{position:absolute;left:234px;top:14px;display:flex;align-items:center;gap:8px}
.brand .mark{width:38px;height:38px;background:var(--red)}
.brand .name{font-size:17px;color:var(--red);font-weight:600;line-height:1}
.brand .name small{display:block;font-size:9px;font-weight:400;margin-top:2px}
.nav span{position:absolute;top:32px;font-size:9px;font-weight:600;letter-spacing:1.2px;color:#777;white-space:nowrap}
.nav .active{color:var(--red);border-bottom:1px solid var(--red);padding-bottom:2px}
.nav-search{position:absolute;left:950px;top:33px;width:10px;height:10px;border:1.5px solid #888;border-radius:50%}

/* hero */
.hero{left:0;top:99px;width:1200px;height:405px;background:linear-gradient(160deg,#8b8478 0%,#5c5953 45%,#6f4a34 75%,#3d3a37 100%)}
.hero-title{position:absolute;left:0;width:1200px;top:100px;text-align:center;font-size:44px;line-height:40px;color:var(--white)}
.hero-text{position:absolute;left:375px;width:450px;top:210px;text-align:center;color:var(--white);font-size:12px;font-weight:700;line-height:19px}
.hero-arrow{position:absolute;top:173px;width:36px;height:36px;border:1.5px solid #fff;border-radius:50%;color:#fff;font-size:16px;display:flex;align-items:center;justify-content:center}

.hex-cta{left:789px;top:391px;width:159px;height:179px}
.hex-cta .txt{position:absolute;left:0;top:40px;width:159px;text-align:center;color:#fff;font-size:12px;line-height:18px}
.hex-cta .cta{position:absolute;left:28px;top:103px;width:100px;height:22px;background:#fff;color:var(--ink);font-family:"Bebas Neue",sans-serif;font-size:13px;display:flex;align-items:center;justify-content:center;letter-spacing:.5px}

/* focus card */
.focus{left:297px;top:466px;width:607px;height:190px;background:var(--white);border-left:1px solid #eee;border-right:1px solid #eee}
.section-title{position:absolute;left:0;width:1200px;text-align:center;font-size:32px}
.focus-text{left:358px;width:484px;top:593px;text-align:center;font-size:11.5px;line-height:19px}
.focus-text strong{display:block;margin-top:16px;color:var(--ink)}

/* requirements */
.side-label{position:absolute;width:44px;height:190px;background:var(--grey-box);display:flex;align-items:center;justify-content:center}
.side-label span{font-family:"Bebas Neue",sans-serif;font-size:17px;letter-spacing:1px;color:var(--ink);white-space:nowrap}
.side-label.left span{transform:rotate(-90deg)}
.side-label.right span{transform:rotate(90deg)}
.req{position:absolute;width:169px;height:41px;background:var(--grey-box);font-family:"Bebas Neue",sans-serif;font-size:18px;letter-spacing:1.5px;color:var(--ink);display:flex;align-items:center;justify-content:center}
.req.to-right{left:297px;clip-path:polygon(0 0,91% 0,100% 50%,91% 100%,0 100%)}
.req.to-left{left:734px;clip-path:polygon(9% 0,100% 0,100% 100%,9% 100%,0 50%)}
.symbol-image{left:520px;top:1000px;width:160px;height:170px;background:linear-gradient(180deg,var(--placeholder-a),var(--placeholder-b))}

/* building blocks */
.blocks-title{left:234px;top:1352px;font-size:33px;line-height:33px;text-align:left}
.block-text{position:absolute;font-size:11.5px;line-height:17.5px}
.block-text h4{font-size:11.5px;font-weight:700;color:var(--ink);margin-bottom:17px}
.block-text ul{list-style:none}
.block-text li{padding-left:12px;position:relative}
.block-text li::before{content:"•";position:absolute;left:0}
.block-text li.sub::before{content:""}
.hex-label{position:absolute;color:#fff;font-size:11.5px;font-weight:700;letter-spacing:.8px;text-align:center;line-height:18px;text-transform:uppercase}

/* photo band */
.band{left:0;top:2142px;width:1200px;height:407px;background:linear-gradient(170deg,#4b5564 0%,#6f7580 40%,#8a8d91 65%,#5b5e63 100%)}
.band-title{position:absolute;left:0;width:1200px;top:94px;text-align:center;color:#fff;font-size:40px;line-height:40px}
.band-text{position:absolute;left:325px;width:550px;top:186px;text-align:center;color:#fff;font-size:12px;font-weight:700;line-height:19px}

/* video */
.video{left:244px;top:2612px;width:712px;height:401px;background:linear-gradient(160deg,#8c8c8c,#4a4a4a 60%,#2a2a2a)}
.video-bar{position:absolute;left:0;top:0;width:712px;height:48px;background:rgba(0,0,0,.85);color:#fff;font-size:12px;font-weight:600;display:flex;align-items:center;padding-left:46px}
.video-bar .dot{position:absolute;left:12px;top:12px;width:24px;height:24px;border-radius:50%;background:#fff}
.video-bar .actions{position:absolute;right:14px;top:10px;display:flex;gap:14px;font-size:8.5px;font-weight:400}
.play{position:absolute;left:331px;top:188px;width:50px;height:50px;border-radius:50%;background:#222}

/* references */
.refs{left:0;top:3090px;width:1200px;height:118px;background:var(--grey-light)}
.refs .label{position:absolute;left:262px;top:52px;font-size:9.5px;font-weight:700;letter-spacing:1.5px;color:#333}
.ref-circle{position:absolute;top:40px;width:36px;height:36px;border:2px solid #777;border-radius:50%}
.ref-name{position:absolute;top:48px;font-size:16px;color:#555}

/* contact */
.contact-band{left:0;top:3208px;width:1200px;height:319px;background:var(--red-dark);color:#fff;text-align:center}
.contact-band .eyebrow{position:absolute;left:0;width:1200px;top:50px;font-size:10px;font-weight:700;letter-spacing:1.5px}
.contact-band .title{position:absolute;left:0;width:1200px;top:78px;font-size:24px;color:#fff;letter-spacing:1.5px}
.contact-band p{position:absolute;left:260px;width:680px;top:128px;font-size:11px;line-height:19px}
.contact-band .field{position:absolute;left:425px;top:182px;width:235px;height:30px;background:#fff;color:#999;font-size:9.5px;text-align:left;padding:9px 14px}
.contact-band .send{left:666px;top:182px;width:110px;height:30px}

.follow{left:465px;top:3556px;display:flex;align-items:center;gap:11px}
.follow .label{font-size:9.5px;font-weight:700;letter-spacing:1.5px;color:#333;margin-right:12px}
.follow span.c{width:26px;height:26px;border-radius:50%;background:var(--red)}

/* footer */
.footer{left:0;top:3621px;width:1200px;height:262px;background:var(--footer);color:#9a9ca6;font-size:9.5px;line-height:15px}
.footer .col{position:absolute;top:106px}
.footer h5{position:absolute;top:60px;color:#fff;font-size:10.5px;font-weight:700;letter-spacing:1.2px}
.footer .brand-f{position:absolute;left:234px;top:40px;display:flex;align-items:center;gap:8px;color:#fff;font-size:13px;line-height:1}
.footer .brand-f .mark{width:34px;height:34px;border:2px solid #fff}
.footer .brand-f small{display:block;font-size:8px;margin-top:2px}
.footer a{color:var(--red)}
.bottom{left:0;top:3883px;width:1200px;height:25px;background:var(--footer-bottom);color:#999;font-size:8.5px;letter-spacing:.8px;text-align:center;padding-top:7px}
</style>
</head>
<body>

<div class="abs topbar">
  <div class="contact">Kontakt +49 (0)12 345 6789 | info@milvetra.de</div>
  <div class="social"><span></span><span></span><span></span></div>
</div>

<header class="abs header">
  <div class="brand"><div class="mark"></div><div class="name">milvetra<small>case engineering</small></div></div>
  <nav class="nav">
    <span class="active" style="left:432px">STARTSEITE</span>
    <span style="left:528px">KOMPETENZEN + REFERENZEN</span>
    <span style="left:724px">DIE KÖPFE DAHINTER</span>
    <span style="left:872px">KONTAKT</span>
  </nav>
  <div class="nav-search"></div>
</header>

<section class="abs hero" role="img" aria-label="Foto eines Containerterminals mit Hafenkränen und Fahrzeugen">
  <h1 class="display hero-title">INDIVIDUELLE KOMPONENTEN<br>UND TECHNISCHE ANLAGEN</h1>
  <p class="hero-text">milvetra entwickelt und konstruiert maßgeschneiderte Batteriegehäuse, die selbst den härtesten Bedingungen standhalten und Batteriemodule und Elektronik zuverlässig schützen.</p>
  <div class="hero-arrow" style="left:18px">‹</div>
  <div class="hero-arrow" style="left:1144px">›</div>
</section>

<div class="abs focus"></div>

<div class="abs hex-cta">
  <svg width="159" height="179" viewBox="0 0 159 179"><polygon points="79.5,0 159,45 159,134 79.5,179 0,134 0,45" fill="var(--red)"/></svg>
  <div class="txt">Jetzt Ihr<br>Fahrzeug <b>ausrüsten</b><br>oder <b>nachrüsten!</b></div>
  <div class="cta">ANFRAGE SENDEN ››</div>
</div>

<h2 class="display section-title" style="top:530px">BATTERIEGEHÄUSE IM FOKUS</h2>
<div class="abs focus-text">
  Im Zeitalter der Elektromobilität kommen gänzlich neue Anforderungen auf die Energieversorgung von elektrisch betriebenen Fahrzeugen zu, die abseits von asphaltierten Straßen zu Hause sind. Off-Highway Fahrzeuge in Logistik, Landwirtschaft, Bauwesen, Berg- und Minenbau werden oftmals unter extremen Bedingungen eingesetzt und müssen dort zuverlässig ihre Aufgaben erfüllen.
  <strong>Dabei kommt dem Schutz von Batteriemodulen, Steuerungselektronik und Batterie-Management-System eine wichtige Aufgabe zu.</strong>
</div>
<div class="btn" style="left:531px;top:778px;width:138px;height:30px">MEHR ERFAHREN</div>

<h2 class="display section-title" style="top:900px">ANFORDERUNGEN AN BATTERIEGEHÄUSE</h2>
<div class="side-label left" style="left:234px;top:995px"><span>TECHNISCHE EINFLÜSSE</span></div>
<div class="req to-right" style="top:995px">FORM</div>
<div class="req to-right" style="top:1045px">GEWICHT</div>
<div class="req to-right" style="top:1095px">VOLUMEN</div>
<div class="req to-right" style="top:1146px">STABILITÄT</div>
<div class="abs symbol-image" role="img" aria-label="Platz für ein Foto als Sinnbild für eine schützende Hülle"></div>
<div class="req to-left" style="top:995px">WASSER</div>
<div class="req to-left" style="top:1045px">STAUB</div>
<div class="req to-left" style="top:1095px">HITZE</div>
<div class="req to-left" style="top:1146px">KÄLTE</div>
<div class="side-label right" style="left:921px;top:995px"><span>UMWELTEINFLÜSSE</span></div>
<div class="btn" style="left:531px;top:1220px;width:138px;height:30px">MEHR ERFAHREN</div>

<h2 class="display abs blocks-title">BAUSTEINE UNSERER<br>BATTERIEGEHÄUSE</h2>

<svg class="abs" style="left:0;top:0" width="1200" height="2000" viewBox="0 0 1200 2000">
  <defs>
    <clipPath id="clip-b"><polygon points="537,1573.5 653,1640 653,1774 537,1840.5 421,1774 421,1640"/></clipPath>
  </defs>
  <polygon points="663,1356.5 779,1423 779,1557 663,1623.5 547,1557 547,1423" fill="var(--red)"/>
  <polygon points="724,1676.5 840,1743 840,1877 724,1943.5 608,1877 608,1743" fill="#cfcfcf"/>
  <polygon points="537,1573.5 653,1640 653,1774 537,1840.5 421,1774 421,1640" fill="var(--red-deep)"/>
  <polygon points="724,1676.5 840,1743 840,1877 724,1943.5 608,1877 608,1743" fill="#3a0a0c" clip-path="url(#clip-b)"/>
  <g fill="none" stroke="#fff" stroke-width="2">
    <circle cx="662" cy="1458" r="16"/><circle cx="662" cy="1458" r="10"/><circle cx="662" cy="1458" r="4"/>
    <line x1="662" y1="1458" x2="678" y2="1442"/>
  </g>
  <line x1="655" y1="1528" x2="671" y2="1528" stroke="#fff" stroke-width="1.5"/>
  <g stroke="#fff" stroke-width="2.5" stroke-linecap="round">
    <line x1="524" y1="1648" x2="550" y2="1674"/><line x1="550" y1="1648" x2="524" y2="1674"/>
  </g>
  <line x1="529" y1="1761" x2="545" y2="1761" stroke="#fff" stroke-width="1.5"/>
  <g fill="none" stroke="#fff" stroke-width="2">
    <circle cx="718" cy="1786" r="11"/><circle cx="718" cy="1786" r="4"/>
    <circle cx="736" cy="1768" r="7"/><circle cx="736" cy="1768" r="2.5"/>
  </g>
  <line x1="716" y1="1858" x2="732" y2="1858" stroke="#fff" stroke-width="1.5"/>
</svg>
<div class="hex-label" style="left:583px;top:1492px;width:160px">BAUSTEIN A –<br>ZIELDEFINITION</div>
<div class="hex-label" style="left:457px;top:1695px;width:160px">BAUSTEIN B –<br>KONSTRUKTION +<br>ENTWICKLUNG</div>
<div class="hex-label" style="left:644px;top:1812px;width:160px">BAUSTEIN C –<br>FERTIGUNG</div>

<div class="block-text" style="left:796px;top:1356px;width:170px">
  <h4>Baustein A – Zieldefinition</h4>
  <ul>
    <li>Beratung</li>
    <li>Umwelteinflüsse / Einsatzbe-dingungen</li>
    <li>Dokumentation</li>
    <li>Anschlussmechanik</li>
    <li>Unterstützung bei der Erstel-lung eines Lastenheftes</li>
    <li>Projektmanagement</li>
    <li>Bauraumstudie</li>
    <li>Schnittstellendefinition</li>
    <li class="sub">- mechanisch</li>
    <li class="sub">- elektrisch</li>
    <li>Erarbeitung eines Pflichten-hefts</li>
  </ul>
</div>
<div class="block-text" style="left:234px;top:1571px;width:170px">
  <h4>Baustein B – Konstruktion +<br>Entwicklung</h4>
  <ul>
    <li>Vorkonstruktion</li>
    <li>Erarbeitung Dichtigkeitskon-zept entsprechend gefor-derter Schutzart</li>
    <li>Simulation</li>
    <li class="sub">- Finite Elemente</li>
    <li class="sub">- Dynamische Lasten</li>
    <li>Fertigungsgerechte Detail-konstruktion</li>
  </ul>
</div>
<div class="block-text" style="left:484px;top:1938px;width:220px">
  <h4>Baustein C – Fertigung</h4>
  <ul>
    <li>Prototypenbau</li>
    <li>Vorserienbau</li>
    <li>Serienproduktion</li>
    <li>Dichtigkeitsprüfung</li>
    <li>Dichtigkeitszertifikat (PNZ / KSA)</li>
  </ul>
</div>

<section class="abs band" role="img" aria-label="Foto eines schweren Off-Highway-Transportfahrzeugs auf einer Baustelle">
  <h2 class="display band-title">VIELFÄLTIGE ANFORDERUNGEN<br>AN BATTERIEGEHÄUSE</h2>
  <p class="band-text">Lorem ipsum dolor sit amet, consetetur sadipscing elitr, sed diam nonumy eirmod tempor invidunt ut labore et dolore magna aliquyam erat, sed diam voluptua. At vero eos et accusam et justo duo dolores et ea rebum</p>
  <div class="btn" style="left:531px;top:287px;width:138px;height:30px">MEHR ERFAHREN</div>
</section>

<div class="abs video" role="img" aria-label="Video-Standbild eines geschlossenen Batteriegehäuses aus Metall">
  <div class="video-bar"><span class="dot"></span>Individuelle technischen Komponenten und Anlagen von milvetra
    <div class="actions"><span>Später ansehen</span><span>Teilen</span></div>
  </div>
  <div class="play"><svg width="50" height="50"><polygon points="21,18 33,25 21,32" fill="#fff"/></svg></div>
</div>

<section class="abs refs">
  <div class="label">REFERENZEN:</div>
  <div class="ref-circle" style="left:362px"></div>
  <div class="ref-name" style="left:442px">Valdoria Motors</div>
  <div class="ref-name" style="left:602px;font-weight:700">Korvath</div>
  <div class="ref-name" style="left:734px">Valdoria Motors</div>
  <div class="ref-circle" style="left:897px"></div>
</section>

<section class="abs contact-band">
  <div class="eyebrow">KONTAKT</div>
  <h2 class="display title">SIE HABEN FRAGEN ZU UNSEREN PRODUKTEN?</h2>
  <p>Lorem ipsum dolor sit amet, consetetur sadipscing elitr, sed diam nonumy eirmod tempor invidunt ut labore et dolore magna aliquyam erat, sed diam voluptua. At vero eos et accusam et justo duo dolores et ea rebum stet clita kasd</p>
  <div class="field">Ihre E-Mail eingeben ...</div>
  <div class="btn send">ABSENDEN</div>
</section>

<div class="abs follow"><span class="label">FOLLOW US:</span><span class="c"></span><span class="c"></span><span class="c"></span><span class="c"></span><span class="c"></span></div>

<footer class="abs footer">
  <div class="brand-f"><div class="mark"></div><div>milvetra<small>case engineering</small></div></div>
  <div class="col" style="left:234px;width:170px">milvetra entwickelt und konstruiert maßgeschneiderte Batteriegehäuse, die selbst den härtesten Bedin-gungen standhalten und Batteriemo-dule und Elektronik zuverlässig schützen.<br>© 2020 All Rights Reserved.</div>
  <h5 style="left:422px">KONTAKT</h5>
  <div class="col" style="left:422px">milvetra<br>Musterstrasse 100<br>12345 Musterstadt<br>Fon: +49 1234 56789 00<br>Fax: +49 1234 56789 00<br>E-Mail: <a>info@milvetra.de</a><br>www.milvetra.de</div>
  <h5 style="left:608px">ÜBER UNS</h5>
  <div class="col" style="left:608px">Milvetra<br>Produkte<br>Support Service<br>Newsletter<br>Kontakt<br>Disclaimer<br>Impressum</div>
  <h5 style="left:796px">PRODUKTE</h5>
  <div class="col" style="left:796px">Baustein A<br>Baustein B<br>Baustein C</div>
</footer>
<div class="abs bottom">COPYRIGHT © 2020 MILVETRA | MUSTERSTRASSE 10 | 12345 MUSTERSTADT | TEL.: 012 345 678 | FAX 012 345 678 | INFO@MILVETRA.DE</div>

</body>
</html>
```